Business card for boutique investment firm

Need a business card designed for our boutique investment firm called "BrightLedger Investment Fee Advisors". We help investors achieve lower fees through negotiation on their behalf. We have a logo to work with and a color palette. The card should incorporate our tag line "The power of small changes" and space for relevant details. The look and feel should reflect the logo and our brand personality: Humble, Trustworthy, Friendly

Target Market(s)

High net worth investors who are looking for clarity around how they are being charged by their investment advisor

Industry/Entity Type

Boutique

Requirements
Must have
• Logo
Tag line: The Power of Small Changes
Space for relevant contact details: name, title, phone, email, URL, mailing address

Use these fonts: 'AvantGarde Bk BT' and 'AvantGarde Bk BT Demi'
Use these colors:
Orange = C-0 / M-60 / Y-100 / K-0
Grey = C-0 / M-0 / Y-0 / K-60

```html
<!DOCTYPE html>
<html lang="en">
<head>
<meta charset="utf-8">
<title>BrightLedger Investment Fee Advisors – Business Card</title>
<link rel="stylesheet" href="https://fonts.googleapis.com/css2?family=Questrial&family=Jura:wght@500;700&family=Archivo+Black&display=swap">
<style>
  :root {
    --orange: #f26f21;
    --grey: #808285;
    --grey-dark: #6d6e70;
    --white: #ffffff;
    --ink: #1e1e1e;
    --backdrop: #e9e7e3;
  }
  * { box-sizing: border-box; margin: 0; padding: 0; }
  html, body { width: 1200px; height: 1050px; overflow: hidden; }
  body { background: var(--backdrop); position: relative; }

  .card {
    position: absolute; top: 157px;
    width: 420px; height: 735px;
    background: var(--white);
    overflow: hidden;
    box-shadow: 0 10px 30px rgba(0,0,0,.18);
  }
  .card--front { left: 150px; }
  .card--back  { left: 630px; }

  /* front */
  .top-strip { position: absolute; left: 0; top: 0; width: 100%; height: 14px; background: var(--grey); }
  .rule { position: absolute; left: 0; width: 100%; height: 6px; background: var(--orange); }
  .rule--upper { top: 14px; }
  .rule--lower { top: 150px; height: 7px; }

  .brand {
    position: absolute; top: 44px; right: 28px;
    display: flex; align-items: center; gap: 10px;
  }
  .brand__dot { width: 46px; height: 46px; border-radius: 50%; background: var(--orange); flex: none; }
  .brand__text { display: flex; flex-direction: column; }
  .brand__name {
    font-family: "Questrial", sans-serif; font-size: 38px; line-height: 1;
    color: var(--orange); letter-spacing: -0.5px;
  }
  .brand__sub {
    font-family: "Questrial", sans-serif; font-size: 12px; color: var(--grey);
    letter-spacing: 1px; margin-top: 3px;
  }
  .tagline {
    position: absolute; top: 118px; right: 28px;
    font-family: "Questrial", sans-serif; font-size: 13px; color: var(--grey-dark);
    letter-spacing: 1.5px; text-transform: uppercase;
  }

  .contact-panel { position: absolute; left: 0; top: 157px; width: 100%; height: 443px; background: var(--grey); }
  .tree { position: absolute; left: 0; top: 0; }

  .box {
    position: absolute; left: 130px; width: 262px;
    border: 2px solid var(--white);
    display: flex; flex-direction: column; align-items: center; justify-content: center;
    color: var(--white); text-align: center;
  }
  .box--name { top: 28px; height: 80px; background: var(--white); color: var(--ink); border-color: var(--white); }
  .box--phone { top: 133px; height: 70px; }
  .box--email { top: 228px; height: 70px; }
  .box--web   { top: 323px; height: 70px; }

  .person__name { font-family: "Archivo Black", sans-serif; font-size: 26px; letter-spacing: 0.5px; }
  .person__title { font-family: "Jura", sans-serif; font-weight: 700; font-size: 14px; margin-top: 2px; }
  .box__label { font-family: "Archivo Black", sans-serif; font-size: 16px; letter-spacing: 0.5px; }
  .box__value { font-family: "Jura", sans-serif; font-weight: 500; font-size: 15px; margin-top: 3px; letter-spacing: 0.5px; }

  .sheen {
    position: absolute; left: 0; top: 600px; width: 100%; height: 7px;
    background: linear-gradient(90deg, #5d5e60, #d9dadb 45%, #ffffff 60%, #8c8d8f);
  }
  .address-band { position: absolute; left: 0; top: 607px; width: 100%; height: 128px; background: var(--orange); }
  .address {
    font-family: "Jura", sans-serif; font-weight: 700; font-size: 16px;
    color: var(--white); letter-spacing: 0.8px;
    position: absolute; left: 22px; top: 22px;
  }

  /* back */
  .back-tagline {
    position: absolute; left: 0; top: 195px; width: 100%;
    text-align: center;
    font-family: "Questrial", sans-serif; font-size: 26px; line-height: 1.4;
    color: var(--grey-dark); letter-spacing: 1px;
  }
  .back-band { position: absolute; left: 0; top: 430px; width: 100%; height: 305px; background: var(--orange); }
  .back-address {
    position: absolute; left: 36px; top: 40px;
    font-family: "Jura", sans-serif; font-weight: 700; font-size: 22px; line-height: 1.6;
    color: var(--white); letter-spacing: 0.8px;
  }
</style>
</head>
<body>

<section class="card card--front" aria-label="Card front">
  <div class="top-strip"></div>
  <div class="rule rule--upper"></div>

  <header class="brand">
    <span class="brand__dot"></span>
    <div class="brand__text">
      <span class="brand__name">BrightLedger</span>
      <span class="brand__sub">Investment Fee Advisors</span>
    </div>
  </header>
  <p class="tagline">The Power of Small Changes</p>

  <div class="rule rule--lower"></div>

  <div class="contact-panel">
    <svg class="tree" width="420" height="443" viewBox="0 0 420 443" aria-hidden="true">
      <g fill="none" stroke="#ffffff" stroke-width="2">
        <path d="M40 20 V358"/>
        <path d="M40 20 H130"/>
        <path d="M40 168 H130"/>
        <path d="M40 263 H130"/>
        <path d="M40 358 H130"/>
      </g>
    </svg>

    <div class="box box--name">
      <span class="person__name">DANIEL REYES</span>
      <span class="person__title">Managing Director</span>
    </div>
    <div class="box box--phone">
      <span class="box__label">PHONE</span>
      <span class="box__value">012 555 0147</span>
    </div>
    <div class="box box--email">
      <span class="box__label">EMAIL</span>
      <span class="box__value">hello@brightledger.com</span>
    </div>
    <div class="box box--web">
      <span class="box__label">WEBSITE</span>
      <span class="box__value">www.brightledger.com</span>
    </div>
  </div>

  <div class="sheen"></div>
  <footer class="address-band">
    <p class="address">027.9th floor,Harbor View Road LKG</p>
  </footer>
</section>

<section class="card card--back" aria-label="Card back">
  <p class="back-tagline">The Power of<br>Small Changes</p>
  <div class="back-band">
    <p class="back-address">027.9th floor,Harbor<br>View Road LKG</p>
  </div>
</section>

</body>
</html>
```